UI Design & Web Design for Used Car Dealer.
Modern and user friendly responsive layout for mobiles and desktop. Bootstrap and form elements for members,registration process,login,dashboard. Layouts for Home Page, Car Listing Pages, Individual Car Information page and etc.

Output files in Bootstrap Html/CSS
Please refer to attachments for more details.

Target Market(s)

Asia / Singapore

Industry/Entity Type

Car Dealer

Coding

Coded - Design and coding required

Number of Pages Required

5+ page

Font styles to use
Sans Serif

Colors
acd037
f6faec
cfcfcf
b1b1b1
ffffff

Requirements
Must have
• Coded in Bootstrap 3 UI Elements, Forms, Labels, Sections, Tables, Buttons, Alerts, Modal, Fonts, Dashboard, Login, Register,Contact
Nice to have
• Stock Images
Should not have
• NA

```html
<!DOCTYPE html>
<html lang="en">
<head>
<meta charset="utf-8">
<title>Sign Up</title>
<link rel="stylesheet" href="https://fonts.googleapis.com/css2?family=Roboto:wght@400;500&family=Open+Sans:wght@400;600;700&display=swap">
<style>
  :root {
    --green: #73bf00;
    --ink: #333333;
    --label: #4a4a4a;
    --muted: #8a8a8a;
    --field: #f0f0f4;
    --rule: #e4e4e4;
    --white: #ffffff;
    --footer: #0a0c0b;
  }
  * { box-sizing: border-box; margin: 0; padding: 0; }
  html, body { width: 1200px; height: 840px; overflow: hidden; }
  body { position: relative; background: var(--white); font-family: "Roboto", sans-serif; color: var(--ink); }

  .hero {
    position: absolute; left: 0; top: 0; width: 1200px; height: 159px;
    background:
      radial-gradient(ellipse 180px 60px at 770px 80px, rgba(150,20,30,.35), transparent),
      radial-gradient(ellipse 200px 80px at 40px 140px, rgba(90,110,20,.5), transparent),
      linear-gradient(180deg, #1b1f22 0%, #2c3236 45%, #15181a 100%);
  }
  .hero-shade { position: absolute; inset: 0; background: rgba(0,0,0,.25); }

  .logo { position: absolute; left: 89px; top: 16px; font-family: "Roboto", sans-serif; font-weight: 500; font-size: 17px; color: var(--white); letter-spacing: .2px; }

  .main-nav { position: absolute; left: 528px; top: 0; display: flex; height: 47px; }
  .main-nav a { font-family: "Open Sans", sans-serif; font-size: 12px; color: var(--white); text-decoration: none; padding: 18px 12px 0; height: 47px; }
  .main-nav a.is-active { color: var(--green); border-bottom: 2px solid var(--green); }

  .social-top { position: absolute; left: 1056px; top: 12px; display: flex; gap: 6px; }
  .social-top span { width: 25px; height: 25px; border-radius: 50%; border: 1px solid var(--white); }
  .social-top span.is-filled { background: var(--green); border-color: var(--green); }

  .page-title { position: absolute; left: 0; width: 1200px; top: 80px; text-align: center; color: var(--white); font-size: 24px; font-weight: 400; }
  .breadcrumb { position: absolute; left: 0; width: 1200px; top: 129px; text-align: center; color: var(--white); font-family: "Open Sans", sans-serif; font-size: 11px; font-weight: 600; }

  .card {
    position: absolute; left: 216px; top: 204px; width: 769px; height: 543px;
    background: var(--white); box-shadow: 0 0 10px rgba(0,0,0,.12);
    padding: 0 43px;
  }
  .card-head { display: flex; justify-content: space-between; align-items: center; height: 65px; border-bottom: 1px solid var(--rule); }
  .card-title { font-size: 23px; font-weight: 400; color: var(--ink); margin-top: 3px; }
  .social-login { display: flex; gap: 9px; margin-top: 2px; }
  .btn-social { height: 36px; border-radius: 18px; background: var(--green); color: var(--white); font-family: "Open Sans", sans-serif; font-size: 12px; font-weight: 600; display: flex; align-items: center; padding: 0 17px; gap: 8px; }
  .btn-social i { width: 10px; height: 10px; border-radius: 50%; background: var(--white); }
  .btn-round { width: 36px; height: 36px; border-radius: 50%; border: 1px solid var(--rule); display: flex; align-items: center; justify-content: center; }
  .btn-round i { width: 8px; height: 8px; border-radius: 50%; background: var(--green); }

  .form { margin-top: 22px; }
  .row { display: flex; gap: 16px; margin-bottom: 27px; }
  .field { flex: 1; }
  .field label { display: flex; align-items: center; gap: 6px; font-size: 14px; color: var(--label); height: 16px; margin-bottom: 8px; }
  .field label svg { width: 12px; height: 12px; stroke: #777; fill: none; stroke-width: 1.2; }
  .input { height: 36px; background: var(--field); font-family: "Open Sans", sans-serif; font-size: 12px; color: #666; display: flex; align-items: center; justify-content: space-between; padding: 0 17px; }
  .input svg { width: 11px; height: 11px; stroke: #555; fill: none; stroke-width: 1.5; }

  .login-hint { display: flex; align-items: center; justify-content: center; gap: 10px; margin-top: -5px; font-size: 13px; }
  .login-hint .link { color: var(--green); display: flex; align-items: center; gap: 9px; }
  .login-hint svg { width: 13px; height: 10px; stroke: var(--green); fill: none; stroke-width: 1.3; }
  .toggle { width: 28px; height: 8px; border-radius: 4px; background: #e2e2e2; position: relative; margin: 0 4px 0 8px; }
  .toggle::before { content: ""; position: absolute; left: -1px; top: -3px; width: 13px; height: 13px; border-radius: 50%; background: #8c8c8c; }
  .login-hint .login-text { font-family: "Open Sans", sans-serif; font-size: 12px; color: #777; }

  .btn-submit { display: flex; align-items: center; justify-content: center; gap: 12px; margin: 23px auto 0; width: 190px; height: 36px; border-radius: 18px; background: var(--green); color: var(--white); font-family: "Open Sans", sans-serif; font-weight: 600; font-size: 13px; }
  .btn-submit svg { width: 13px; height: 10px; stroke: var(--white); fill: none; stroke-width: 1.4; }

  .footer { position: absolute; left: 0; top: 789px; width: 1200px; height: 51px; background: var(--footer); color: var(--white); font-family: "Open Sans", sans-serif; font-size: 11px; font-weight: 600; text-align: center; line-height: 51px; }
</style>
</head>
<body>
  <header class="hero" role="img" aria-label="Blurred photo of cars on a dealer lot">
    <div class="hero-shade"></div>
  </header>

  <div class="logo">LOGO HERE</div>
  <nav class="main-nav">
    <a class="is-active">HOME</a><a>BENEFITS</a><a>VEHICLE</a><a>LISTINGS</a><a>START ADVERTISING NOW</a><a>CONTACT</a>
  </nav>
  <div class="social-top"><span></span><span class="is-filled"></span></div>

  <h1 class="page-title">SIGN UP</h1>
  <div class="breadcrumb">HOME / SIGN UP</div>

  <main class="card">
    <div class="card-head">
      <h2 class="card-title">Sign up</h2>
      <div class="social-login">
        <div class="btn-social"><i></i>Quill</div>
        <div class="btn-round"><i></i></div>
      </div>
    </div>

    <div class="form">
      <div class="row">
        <div class="field">
          <label><svg viewBox="0 0 12 12"><path d="M2.5 1h5l2 2v8h-7z M4 6h4 M4 8h4"/></svg>Title</label>
          <div class="input">Select <svg viewBox="0 0 12 12"><path d="M2 4l4 4 4-4"/></svg></div>
        </div>
      </div>
      <div class="row">
        <div class="field">
          <label><svg viewBox="0 0 12 12"><circle cx="6" cy="4" r="2.5"/><path d="M1.5 11.5c0-3 2-4.5 4.5-4.5s4.5 1.5 4.5 4.5"/></svg>First Name:</label>
          <div class="input">Enter Your Name</div>
        </div>
        <div class="field">
          <label><svg viewBox="0 0 12 12"><circle cx="6" cy="4" r="2.5"/><path d="M1.5 11.5c0-3 2-4.5 4.5-4.5s4.5 1.5 4.5 4.5"/></svg>Last Name:</label>
          <div class="input">Enter Your Name</div>
        </div>
      </div>
      <div class="row">
        <div class="field">
          <label><svg viewBox="0 0 12 12"><rect x="1" y="2.5" width="10" height="7"/><path d="M1 2.5l5 4 5-4 M1 9.5l3.5-3.5 M11 9.5l-3.5-3.5"/></svg>Email:</label>
          <div class="input">Enter Your Email</div>
        </div>
        <div class="field">
          <label><svg viewBox="0 0 12 12"><path d="M2 1.5l2 0 1 2.5-1.3 1a6 6 0 0 0 3.3 3.3l1-1.3 2.5 1v2c-5 0-8.5-3.5-8.5-8.5z M7 1a4 4 0 0 1 4 4 M7 3a2 2 0 0 1 2 2"/></svg>Mobile Phone Number</label>
          <div class="input">Phone Number</div>
        </div>
      </div>
      <div class="row">
        <div class="field">
          <label><svg viewBox="0 0 12 12"><rect x="2" y="5.5" width="8" height="6"/><path d="M3.5 5.5v-2a2.5 2.5 0 0 1 5 0v2"/></svg>Password</label>
          <div class="input">***********</div>
        </div>
        <div class="field">
          <label><svg viewBox="0 0 12 12"><rect x="2" y="5.5" width="8" height="6"/><path d="M3.5 5.5v-2a2.5 2.5 0 0 1 5 0v2"/></svg>Confirm Password</label>
          <div class="input">***********</div>
        </div>
      </div>

      <div class="login-hint">
        <span class="link">Already registered? <svg viewBox="0 0 13 10"><path d="M1 5h11 M8 1l4 4-4 4"/></svg></span>
        <span class="toggle"></span>
        <span class="login-text">Login Here</span>
      </div>

      <div class="btn-submit">Submit <svg viewBox="0 0 13 10"><path d="M1 5h11 M8 1l4 4-4 4"/></svg></div>
    </div>
  </main>

  <footer class="footer">COPYRIGHT 2016. ALL RIGHT RESERVED</footer>
</body>
</html>
```